LOCAL TAXI SERVICE NEEDS A BANNER AD DESIGN

NEED BANNER AD DESIGN FOR TAXI SERVICE IN NJ. WE PROVIDE LOCAL AND LONG DISTANCE TRANSPORTATION. OUR MAIN BASE OF CUSTOMER GO TO THE MAJOR AIRPORTS IN THE TRI STATE AREA. I WANT TO OFFER A SPECIAL GOING TO HOLMBRIDGE AIRPORT OF $35.00 WITH A COUPON CODE OF PW 12. THIS BANNER AD WILL BE USED FOR MY PALWIRE PAGE

Target Market(s)

PEOPLE WHO TRAVEL A LOT

Industry/Entity Type

Taxi

Font styles to use
Serif
Sans Serif

Colors
0792cd
0255a3
33a6d7
85cae6
cee9f5
ecf7fb
ffffff

Requirements
Must have
• MY COMPANY NAME: DORVAN'S TAXI

```html
<!DOCTYPE html>
<html lang="en">
<head>
<meta charset="utf-8">
<title>Dorvan's Taxi – Airport Offer Banner</title>
<link rel="stylesheet" href="https://fonts.googleapis.com/css2?family=Arimo:wght@400;700&display=swap">
<style>
  :root {
    --deep-blue: #0255a3;
    --brand-blue: #0792cd;
    --mid-blue: #33a6d7;
    --sky-blue: #85cae6;
    --pale-blue: #cee9f5;
    --ice-blue: #ecf7fb;
    --white: #ffffff;
    --ink: #0b0b0d;
    --royal: #1a2fb8;
  }
  * { margin: 0; padding: 0; box-sizing: border-box; }
  html, body { width: 1200px; height: 444px; overflow: hidden; }
  body { font-family: "Arimo", Arial, sans-serif; }

  .banner {
    position: relative;
    width: 1200px;
    height: 444px;
    overflow: hidden;
    background:
      radial-gradient(circle at 820px 60px, rgba(133,202,230,.55) 0 60px, transparent 110px),
      radial-gradient(circle at 1010px 200px, rgba(133,202,230,.45) 0 50px, transparent 100px),
      radial-gradient(circle at 1130px 80px, rgba(206,233,245,.45) 0 45px, transparent 90px),
      radial-gradient(circle at 620px 380px, rgba(133,202,230,.35) 0 50px, transparent 100px),
      radial-gradient(circle at 120px 420px, rgba(133,202,230,.35) 0 40px, transparent 90px),
      radial-gradient(ellipse at 60% 40%, var(--mid-blue), var(--brand-blue) 45%, var(--deep-blue) 100%);
  }

  /* Left card */
  .service-card {
    position: absolute;
    left: 42px; top: 31px;
    width: 402px; height: 378px;
    background: radial-gradient(ellipse at 50% 45%, #2a2a30, var(--ink) 75%);
  }
  .brand-bar {
    position: absolute;
    left: 10px; top: 10px; width: 382px; height: 62px;
    background: var(--royal);
    display: flex; align-items: center; gap: 12px;
    padding-left: 10px;
  }
  .brand-mark {
    width: 42px; height: 42px;
    background: var(--white);
  }
  .brand-name {
    color: var(--white);
    font-weight: 400;
    font-size: 36px;
    letter-spacing: 1px;
    white-space: nowrap;
  }
  .vehicle-photo {
    position: absolute;
    left: 40px; top: 95px; width: 322px; height: 190px;
    border-radius: 30px 60px 20px 20px;
    background: linear-gradient(180deg, #f4f6f8, #c9ced3 70%, #6b7076);
  }
  .service-title {
    position: absolute;
    left: 0; right: 0; top: 291px;
    text-align: center;
    color: var(--royal);
    font-weight: 700;
    font-size: 19px;
    letter-spacing: .5px;
    text-shadow: 0 0 2px var(--white), 0 0 1px var(--white);
  }
  .service-address {
    position: absolute;
    left: 0; right: 0; top: 322px;
    text-align: center;
    color: var(--pale-blue);
    font-size: 12px;
    letter-spacing: 1px;
  }
  .service-phone {
    position: absolute;
    left: 125px; top: 343px; width: 152px; height: 25px;
    background: var(--royal);
    border: 2px solid var(--white);
    color: var(--white);
    font-weight: 700; font-size: 15px;
    display: flex; align-items: center; justify-content: center;
  }

  /* Offer copy */
  .offer {
    position: absolute; left: 500px; top: 104px;
    color: var(--sky-blue);
    font-weight: 700;
    text-shadow: 0 0 6px rgba(206,233,245,.6);
  }
  .offer-heading { font-size: 34px; line-height: 40px; margin-bottom: 20px; }
  .offer-text { font-size: 26px; line-height: 53px; }
  .offer-text .lead { font-size: 32px; }

  .coupon {
    position: absolute;
    left: 500px; top: 289px; width: 683px; height: 75px;
    border-radius: 38px;
    background: linear-gradient(180deg, var(--sky-blue), var(--mid-blue) 55%, var(--brand-blue));
    box-shadow: inset 0 2px 3px rgba(236,247,251,.7), 0 2px 6px rgba(2,85,163,.5);
    display: flex; align-items: center;
    padding-left: 22px;
    color: var(--white);
    font-weight: 700;
    white-space: nowrap;
  }
  .coupon-big { font-size: 30px; margin-right: 10px; }
  .coupon-small { font-size: 23px; }
  .coupon-arrow {
    position: absolute; right: 12px; top: 14px;
    width: 48px; height: 48px;
  }
</style>
</head>
<body>
  <div class="banner">
    <section class="service-card">
      <div class="brand-bar">
        <span class="brand-mark"></span>
        <span class="brand-name">DORVAN'S TAXI</span>
      </div>
      <div class="vehicle-photo" role="img" aria-label="White passenger minivan used as a taxi"></div>
      <div class="service-title">TAXI TRANSPORTATION SERVICE</div>
      <div class="service-address">42 LARKSPUR AVENUE FENWICK NJ 07001</div>
      <div class="service-phone">(555) 014-2260</div>
    </section>

    <div class="offer">
      <p class="offer-heading">NEW OFFER!!</p>
      <p class="offer-text"><span class="lead">D</span>ORVAN'S TAXI offering special going to</p>
      <p class="offer-text">Holmbridge Airport for</p>
    </div>

    <div class="coupon">
      <span class="coupon-big">ONLY</span>
      <span class="coupon-small">35$ WITH A COUPON CODE OF PW 12</span>
      <svg class="coupon-arrow" viewBox="0 0 48 48" aria-hidden="true">
        <circle cx="24" cy="24" r="23" fill="#0255a3" stroke="#85cae6" stroke-width="2"/>
        <path d="M19 14 L33 24 L19 34 Z" fill="#ffffff"/>
      </svg>
    </div>
  </div>
</body>
</html>
```